Webdesign für Arztpraxis
Zielgruppe
Arztpraxis für Dermatologie am Lindwarte.
Lindwarte ist ein Spital/Krankenhaus hier in Basel, Schweiz.
Kunden sind in jeder Altersstufe für Hauterkrankungen.
Behandlung Chirugisch, konservativ und mit Laser.
Aufgabenstellung
Brandguide und Logo anbei
Farben: #395722 und #ABCF8A
Beispielseite, die gefällt: https://hautarztpraxis-morvel-quandt.de

```html
<!DOCTYPE html>
<html lang="de">
<head>
<meta charset="utf-8">
<title>Dermatologie am Lindwarte</title>
<link href="https://fonts.googleapis.com/css2?family=Poppins:wght@400;500;600;700&display=swap" rel="stylesheet">
<style>
:root{
  --green-dark:#395722;
  --green-light:#abcf8a;
  --ink:#141414;
  --text:#3a3a3a;
  --white:#ffffff;
  --sky:#eaf4fd;
  --page:#f3f7ee;
}
*{box-sizing:border-box;margin:0;padding:0}
html,body{width:1200px;height:698px;overflow:hidden;background:var(--page);font-family:'Poppins',sans-serif;color:var(--ink)}
.site{position:relative;width:1200px;height:698px;overflow:hidden;background:var(--sky)}
.hero{position:absolute;left:0;top:0;width:1200px;height:520px;
  background:linear-gradient(100deg,#cfc6bb 0%,#ddd6cf 22%,#e6e1dc 40%,#a89a8f 52%,#6f7a55 64%,#4f6a36 78%,#3f5a2c 100%)}
.header{position:absolute;left:166px;top:11px;width:868px;height:70px;background:var(--white);border-radius:4px;box-shadow:0 2px 8px rgba(0,0,0,.08)}
.brand{position:absolute;left:18px;top:14px;display:flex;align-items:center;gap:10px}
.brand-dot{width:40px;height:40px;border-radius:50%;background:var(--green-light)}
.brand-name{font-size:20px;font-weight:500;color:var(--green-dark);line-height:1.05}
.brand-name small{display:block;font-size:13px;font-weight:500}
.nav{position:absolute;left:301px;top:46px;display:flex;gap:16px;font-size:10.5px}
.nav a{color:var(--ink);text-decoration:none}
.nav a.active{color:var(--green-light);border-bottom:1px solid var(--green-light);padding-bottom:3px}
.info{position:absolute;top:12px;display:flex;align-items:center;gap:5px;font-size:8px;line-height:1.15;color:#555}
.info.hours{left:463px}
.info.phone{left:602px;padding-left:18px;border-left:1px solid #e6e6e6}
.info b{font-weight:400;font-size:9.5px;color:var(--ink)}
.header-cta{position:absolute;left:709px;top:8px;width:151px;height:29px;border:1px solid var(--green-light);border-radius:15px;display:flex;align-items:center;justify-content:center;gap:28px;font-size:10px;color:var(--green-light);padding-left:14px}
.welcome{position:absolute;left:585px;top:100px;width:330px;height:330px;border-radius:50%;background:var(--white);display:flex;flex-direction:column;align-items:center;justify-content:center;text-align:center}
.ring{position:absolute;left:570px;top:85px;width:360px;height:360px;border-radius:50%;border:1px dashed rgba(255,255,255,.85)}
.welcome h1{font-size:26px;font-weight:600;line-height:1.3;margin-top:-20px}
.welcome .btn{margin-top:34px;background:var(--green-dark);color:var(--white);font-size:11.5px;font-weight:500;padding:6px 13px;border-radius:14px}
.slide-prev{position:absolute;left:28px;top:234px;width:62px;height:62px;border-radius:50%;background:rgba(120,110,105,.55);display:flex;align-items:center;justify-content:center}
.slide-next{position:absolute;left:1128px;top:250px}
.quick{position:absolute;left:166px;top:494px;display:flex;gap:12px}
.quick-card{width:208px;height:53px;background:var(--white);border-radius:26px;box-shadow:0 3px 10px rgba(0,0,0,.08);display:flex;align-items:center;padding:0 14px 0 18px;font-size:12px;font-weight:500;color:var(--green-dark)}
.quick-card .label{flex:1;display:flex;align-items:center;gap:8px}
.quick-card .label.center{justify-content:center}
.about-portrait{position:absolute;left:166px;top:570px;width:216px;height:140px;border-radius:110px 0 0 0;background:linear-gradient(135deg,#f4f1ee,#e7ddd4)}
.about-text{position:absolute;left:409px;top:573px;width:360px}
.eyebrow{font-size:7.5px;color:var(--green-light)}
.about-text h2{font-size:17px;font-weight:600;margin:2px 0 6px}
.about-text p{font-size:9.3px;line-height:1.68;color:var(--text)}
.about-photo{position:absolute;left:790px;top:598px;width:244px;height:110px;border-radius:3px;background:linear-gradient(90deg,#d9c9a8,#e4d8bf 50%,#c9d6c3)}
</style>
</head>
<body>
<div class="site">
  <div class="hero" role="img" aria-label="Foto: helle Praxisgebäude im Quartier mit grossen grünen Bäumen"></div>

  <header class="header">
    <div class="brand">
      <span class="brand-dot"></span>
      <span class="brand-name">Dermatologie<small>am Lindwarte</small></span>
    </div>
    <div class="info hours">
      <svg width="15" height="15" viewBox="0 0 16 16"><circle cx="8" cy="8" r="6.5" fill="none" stroke="#abcf8a" stroke-width="1.2"/><path d="M8 4.5V8l2.3 1.5" fill="none" stroke="#abcf8a" stroke-width="1.2"/></svg>
      <span><b>MO. - FR.</b><br>10-17 Uhr</span>
    </div>
    <div class="info phone">
      <svg width="15" height="15" viewBox="0 0 16 16"><path d="M3 2h3l1.2 3.2-1.8 1.2a8 8 0 0 0 4.2 4.2l1.2-1.8L14 10v3a1 1 0 0 1-1 1A12 12 0 0 1 2 3a1 1 0 0 1 1-1z" fill="none" stroke="#abcf8a" stroke-width="1.1"/></svg>
      <span>Telefon<br><b>061 000 47 58</b></span>
    </div>
    <a class="header-cta">Online Termin
      <svg width="10" height="8" viewBox="0 0 10 8"><path d="M0 4h8.5M6 1l3 3-3 3" fill="none" stroke="#abcf8a" stroke-width="1"/></svg>
    </a>
    <nav class="nav">
      <a class="active">Home</a><a>Über Uns</a><a>Leistungsspektrum</a><a>Kontakt</a>
    </nav>
  </header>

  <div class="ring"></div>
  <section class="welcome">
    <h1>Herzlich<br>willkommen<br>in der Hautarztpraxis<br>im Hellwiese-Quartier<br>Basel!</h1>
    <span class="btn">Termin online</span>
  </section>

  <div class="slide-prev"><svg width="14" height="26" viewBox="0 0 14 26"><path d="M12 1L2 13l10 12" fill="none" stroke="#fff" stroke-width="1.6"/></svg></div>
  <div class="slide-next"><svg width="14" height="26" viewBox="0 0 14 26"><path d="M2 1l10 12L2 25" fill="none" stroke="#fff" stroke-width="1.6"/></svg></div>

  <div class="quick">
    <div class="quick-card"><span class="label">
      <svg width="24" height="24" viewBox="0 0 24 24"><rect x="2" y="4" width="18" height="16" rx="2" fill="none" stroke="#395722" stroke-width="1.1"/><path d="M2 9h18M7 2v4M15 2v4" stroke="#395722" stroke-width="1.1"/><circle cx="18" cy="19" r="4" fill="#fff" stroke="#abcf8a" stroke-width="1.1"/><path d="M16.3 19l1.2 1.2 2-2.2" fill="none" stroke="#abcf8a" stroke-width="1.1"/></svg>
      Termine Buchen</span>
      <svg width="14" height="10" viewBox="0 0 14 10"><path d="M0 5h12.5M8.5 1l4 4-4 4" fill="none" stroke="#333" stroke-width="1.1"/></svg></div>
    <div class="quick-card"><span class="label">
      <svg width="22" height="22" viewBox="0 0 16 16"><path d="M3 2h3l1.2 3.2-1.8 1.2a8 8 0 0 0 4.2 4.2l1.2-1.8L14 10v3a1 1 0 0 1-1 1A12 12 0 0 1 2 3a1 1 0 0 1 1-1z" fill="none" stroke="#395722" stroke-width="0.9"/></svg>
      Arzt auf Abruf</span>
      <svg width="14" height="10" viewBox="0 0 14 10"><path d="M0 5h12.5M8.5 1l4 4-4 4" fill="none" stroke="#333" stroke-width="1.1"/></svg></div>
    <div class="quick-card"><span class="label center">Anfahrt</span>
      <svg width="14" height="10" viewBox="0 0 14 10"><path d="M0 5h12.5M8.5 1l4 4-4 4" fill="none" stroke="#333" stroke-width="1.1"/></svg></div>
    <div class="quick-card"><span class="label center">Öffnungszeiten</span>
      <svg width="14" height="10" viewBox="0 0 14 10"><path d="M0 5h12.5M8.5 1l4 4-4 4" fill="none" stroke="#333" stroke-width="1.1"/></svg></div>
  </div>

  <div class="about-portrait" role="img" aria-label="Porträtfoto des Praxisarztes"></div>
  <section class="about-text">
    <p class="eyebrow">Über Uns</p>
    <h2>Dermatologie am Lindwarte</h2>
    <p>Dermatologie am Lindwarte ist eine moderne Praxis für allgemeine und ästhetische Dermatologie. Wir behandeln und beraten Sie bei allen Hauterkrankungen, Hautkrebs und Allergien.<br>Wenn es darum geht, sich einfach wieder gut und schön zu fühlen in Ihrer Haut profitieren Sie von unserer Expertise in Lasermedizin und</p>
  </section>
  <div class="about-photo" role="img" aria-label="Foto: Arzt im Beratungsgespräch mit einer Patientin"></div>
</div>
</body>
</html>
```